Mirabo & Orvan Automotive Repair Shop. Need a new website design.

We specialize in Mirabo & Orvan auto repair, but also work on other Asian import vehicles. We have been in business for 7 years and pride ourselves on high quality auto repair that is fixed right the first time. Would like the automotive repair website to incorporate the colors black, red and white if possible and have our logo and some Mirabo and Orvan vehicles included in the website.

Target Market(s)

Mirabo & Orvan vehicle owners

Industry/Entity Type

Automotive Repair

Coding

Coded - Design and coding required

Number of Pages Required

5+ page

Colors
EB3D1F
EC4F4E
F09395
F8D3D4
FCEDEE

Requirements
Must have
• Home, Services, Contact Us, Schedule appointment, and a gallery tab that I can add shop pictures to when completed.
Nice to have
• Would like to see example pictures of job next to each service listed.
Should not have
• Service not related to auto repair. Ex. auto detailing, towing, car wash

```html
<!DOCTYPE html>
<html lang="en">
<head>
<meta charset="utf-8">
<title>Vanta Automotive</title>
<link href="https://fonts.googleapis.com/css2?family=Lato:wght@400;700&display=swap" rel="stylesheet">
<style>
:root{
  --bg:#222226;
  --bg-deep:#1b1c22;
  --red:#d9263c;
  --white:#ffffff;
  --text-dark:#2a2a2e;
  --grey:#b3b3b3;
  --line:#cfcfcf;
}
*{box-sizing:border-box;margin:0;padding:0}
html,body{width:1200px;height:3634px;overflow:hidden}
body{position:relative;background:var(--bg);color:var(--white);font-family:'Lato',sans-serif}
.abs{position:absolute}
a{color:inherit}

/* hero */
.hero{left:0;top:0;width:1200px;height:720px;background:radial-gradient(ellipse at 55% 50%,#4a4b50 0%,#2e2f33 55%,#1f2024 100%)}
.nav{left:0;top:0;width:1200px;height:140px}
.nav-link{top:59px;font-size:16px;letter-spacing:.2px;text-transform:uppercase}
.nav-link.is-active{color:var(--red)}
.brand{left:550px;top:30px;width:100px;height:76px;display:flex;align-items:center;justify-content:center;gap:6px;font-weight:700;font-size:20px;letter-spacing:1px}
.brand-dot{width:10px;height:10px;border-radius:50%;background:var(--red)}
.hero-title{left:0;top:244px;width:1200px;text-align:center;font-weight:700;font-size:40px;line-height:48px}
.hero-sub{left:0;top:368px;width:1200px;text-align:center;font-weight:700;font-size:19px}
.installer-label{left:83px;top:552px;font-size:12px}
.badge{background:#e8e8ea;opacity:.9}

/* intro */
.intro-lead{left:170px;top:800px;width:860px;text-align:center;font-size:25px;line-height:31px}
.intro-body{left:83px;top:1040px;width:430px;font-size:15.5px;line-height:20px}
.intro-body p+p{margin-top:20px}
.slider{left:546px;top:979px;width:571px;height:332px;background:#fff}
.slider-photo{left:0;top:0;width:504px;height:332px;background:radial-gradient(ellipse at 50% 55%,#6b6c70 0%,#9a9ba0 30%,#f2f2f2 60%,#fff 100%)}
.slider-next{left:504px;top:0;width:67px;height:332px;background:#a9a9a9;display:flex;align-items:center;justify-content:center}
.dots{top:1337px;height:3px}
.makes-text{left:200px;top:1426px;width:800px;text-align:center;font-size:18px;line-height:23px}
.make{top:1499px;width:162px;height:84px;background:#fff;color:var(--text-dark);display:flex;align-items:center;justify-content:center;font-weight:700;font-size:20px}
.arrow-btn{top:1526px}

/* services */
.services{left:0;top:1667px;width:1200px;height:578px;background:linear-gradient(180deg,#262834 0%,#1d1f29 100%)}
.services-title{left:0;top:1720px;width:1200px;text-align:center;font-weight:700;font-size:26px}
.service-list{list-style:none;font-size:16px}
.service-list li{height:33.3px;display:flex;align-items:center;gap:12px}
.check{flex:none}
.ask-band{left:0;top:2245px;width:1200px;height:77px;background:#fff;color:var(--text-dark);text-align:center;font-size:19px;line-height:77px}
.ask-band a{text-decoration:underline}

/* contact */
.contact-title{left:83px;top:2488px;font-weight:700;font-size:26px}
.contact-copy{left:83px;top:2534px;width:420px;font-size:18px;line-height:24px}
.contact-alt{left:83px;top:2641px;font-weight:700;font-size:19px}
.contact-click{left:83px;top:2677px;font-size:19px;color:var(--red);text-decoration:underline}
.field{background:#fff;color:#444;font-size:12px;padding:0 14px;display:flex;align-items:center;justify-content:space-between}
.field.is-area{align-items:flex-start;padding-top:14px}
.submit{left:606px;top:2742px;width:511px;height:41px;background:var(--red);color:#fff;font-size:12px;display:flex;align-items:center;justify-content:center}

/* gallery */
.tile{background:radial-gradient(ellipse at 50% 55%,#c9cacd 0%,#eaeaec 45%,#fafafa 100%)}
.tile.is-engine{background:radial-gradient(ellipse at 50% 50%,#4c4d52 0%,#2d2e33 70%)}
.gallery-card{left:345px;top:2867px;width:332px;height:222px;background:#fff;color:var(--text-dark)}
.gallery-title{left:0;top:66px;width:332px;text-align:center;font-weight:700;font-size:26px}
.gallery-btn{left:85px;top:111px;width:161px;height:44px;background:var(--red);color:#fff;font-size:17px;display:flex;align-items:center;justify-content:center;gap:10px}

/* footer */
.footer{left:0;top:3335px;width:1200px;height:299px;background:linear-gradient(180deg,#24262f,#1c1d25)}
.footer-brand{left:168px;top:3410px;width:160px;display:flex;align-items:center;justify-content:center;gap:8px;font-weight:700;font-size:30px;letter-spacing:1px}
.copyright{left:168px;top:3552px;font-size:12px}
.info{left:455px;font-size:16px;line-height:20px;display:flex;gap:14px}
.info svg{flex:none;margin-top:2px}
.quick{right:168px;top:3388px;text-align:right;font-size:16px;line-height:33.5px}
.quick-title{font-weight:700;text-decoration:underline}
</style>
</head>
<body>

<!-- HERO -->
<div class="abs hero" role="img" aria-label="Close view of a V8 engine cover under a dark overlay"></div>
<nav class="abs nav">
  <a class="abs nav-link is-active" style="left:83px">Home</a>
  <a class="abs nav-link" style="left:227px">Services</a>
  <a class="abs nav-link" style="left:395px">Contact Us</a>
  <div class="abs brand"><span class="brand-dot"></span>VANTA</div>
  <a class="abs nav-link" style="left:702px">Gallery</a>
  <a class="abs nav-link" style="left:879px">Schedule an Appointment</a>
</nav>
<h1 class="abs hero-title">“DEALERSHIP QUALITY AT<br>AFFORDABLE PRICES"</h1>
<p class="abs hero-sub">Specializing in Mirabo, Orvan, &amp; Kestrel Auto Repair</p>
<p class="abs installer-label">Authorized installer for</p>
<div class="abs badge" style="left:85px;top:586px;width:124px;height:78px"></div>
<div class="abs badge" style="left:226px;top:606px;width:98px;height:30px"></div>
<div class="abs badge" style="left:937px;top:582px;width:83px;height:83px"></div>
<div class="abs badge" style="left:1038px;top:585px;width:74px;height:74px;border-radius:50%"></div>

<!-- INTRO -->
<p class="abs intro-lead">Vanta Automotive is a locally owned and operated auto repair shop in Ridgeford that offers comprehensive car care and services for Mirabo &amp; Orvan and all other Asian imports vehicles.</p>
<div class="abs intro-body">
  <p>Led by an MTA master certified technician with 20 years experience working for Mirabo &amp; Orvan dealerships, our auto shop is your go to facility for everything from factory auto maintenance, including oil changes, fluid services and tune ups, to complex engine repairs, hybrid diagnostic &amp; repair, brake jobs, etc.</p>
  <p>We have state of the art equipment and tools to ensure that we can properly diagnose and repair your vehicle to get you back on the road quickly. Our work comes with a warranty and we offer towing if needed. We also offer discounts for Rydo &amp; Hopla rides.</p>
</div>
<div class="abs slider">
  <div class="abs slider-photo" role="img" aria-label="Grey Orvan sport sedan on a white backdrop"></div>
  <div class="abs slider-next"><svg width="14" height="24" viewBox="0 0 14 24"><path d="M2 2l10 10L2 22" fill="none" stroke="#fff" stroke-width="3"/></svg></div>
</div>
<div class="abs dots" style="left:775px;width:27px;background:var(--red)"></div>
<div class="abs dots" style="left:805px;width:82px;background:#8a8a8a"></div>

<p class="abs makes-text">Vanta Automotive specializes in Mirabo &amp; Orvan auto repair but also service and repair the following makes:</p>
<svg class="abs arrow-btn" style="left:95px" width="16" height="30" viewBox="0 0 16 30"><path d="M13 3L3 15l10 12" fill="none" stroke="#fff" stroke-width="3"/></svg>
<div class="abs make" style="left:171px">HANKO</div>
<div class="abs make" style="left:345px">AVETA</div>
<div class="abs make" style="left:519px">HYORIN</div>
<div class="abs make" style="left:694px">KAYA</div>
<div class="abs make" style="left:868px">NISORA</div>
<svg class="abs arrow-btn" style="left:1089px" width="16" height="30" viewBox="0 0 16 30"><path d="M3 3l10 12L3 27" fill="none" stroke="#fff" stroke-width="3"/></svg>

<!-- SERVICES -->
<div class="abs services" role="img" aria-label="Dark tyre tread texture background"></div>
<h2 class="abs services-title">Services</h2>
<ul class="abs service-list" style="left:84px;top:1799px">
  <li><svg class="check" width="16" height="16" viewBox="0 0 16 16"><rect x="1" y="2" width="12" height="12" fill="none" stroke="#d9263c" stroke-width="1.6"/><path d="M4 8l3 3 7-8" fill="none" stroke="#d9263c" stroke-width="1.8"/></svg>Automatic, Manual, Computerized Transmission Service &amp; Repair</li>
  <li><svg class="check" width="16" height="16" viewBox="0 0 16 16"><rect x="1" y="2" width="12" height="12" fill="none" stroke="#d9263c" stroke-width="1.6"/><path d="M4 8l3 3 7-8" fill="none" stroke="#d9263c" stroke-width="1.8"/></svg>Brakes Service &amp; Repair</li>
  <li><svg class="check" width="16" height="16" viewBox="0 0 16 16"><rect x="1" y="2" width="12" height="12" fill="none" stroke="#d9263c" stroke-width="1.6"/><path d="M4 8l3 3 7-8" fill="none" stroke="#d9263c" stroke-width="1.8"/></svg>Clutch Service &amp; Repair</li>
  <li><svg class="check" width="16" height="16" viewBox="0 0 16 16"><rect x="1" y="2" width="12" height="12" fill="none" stroke="#d9263c" stroke-width="1.6"/><path d="M4 8l3 3 7-8" fill="none" stroke="#d9263c" stroke-width="1.8"/></svg>Computer Diagnostics</li>
  <li><svg class="check" width="16" height="16" viewBox="0 0 16 16"><rect x="1" y="2" width="12" height="12" fill="none" stroke="#d9263c" stroke-width="1.6"/><path d="M4 8l3 3 7-8" fill="none" stroke="#d9263c" stroke-width="1.8"/></svg>CV Axle Service &amp; Repair</li>
  <li><svg class="check" width="16" height="16" viewBox="0 0 16 16"><rect x="1" y="2" width="12" height="12" fill="none" stroke="#d9263c" stroke-width="1.6"/><path d="M4 8l3 3 7-8" fill="none" stroke="#d9263c" stroke-width="1.8"/></svg>Electrical Specialists</li>
  <li><svg class="check" width="16" height="16" viewBox="0 0 16 16"><rect x="1" y="2" width="12" height="12" fill="none" stroke="#d9263c" stroke-width="1.6"/><path d="M4 8l3 3 7-8" fill="none" stroke="#d9263c" stroke-width="1.8"/></svg>Emission Repair &amp; Catalytic Converters</li>
  <li><svg class="check" width="16" height="16" viewBox="0 0 16 16"><rect x="1" y="2" width="12" height="12" fill="none" stroke="#d9263c" stroke-width="1.6"/><path d="M4 8l3 3 7-8" fill="none" stroke="#d9263c" stroke-width="1.8"/></svg>Engine Repair</li>
  <li><svg class="check" width="16" height="16" viewBox="0 0 16 16"><rect x="1" y="2" width="12" height="12" fill="none" stroke="#d9263c" stroke-width="1.6"/><path d="M4 8l3 3 7-8" fill="none" stroke="#d9263c" stroke-width="1.8"/></svg>Exhaust, Muffler Service &amp; Repair</li>
  <li><svg class="check" width="16" height="16" viewBox="0 0 16 16"><rect x="1" y="2" width="12" height="12" fill="none" stroke="#d9263c" stroke-width="1.6"/><path d="M4 8l3 3 7-8" fill="none" stroke="#d9263c" stroke-width="1.8"/></svg>Fuel Injection System Service, Cleaning &amp; Repair</li>
  <li><svg class="check" width="16" height="16" viewBox="0 0 16 16"><rect x="1" y="2" width="12" height="12" fill="none" stroke="#d9263c" stroke-width="1.6"/><path d="M4 8l3 3 7-8" fill="none" stroke="#d9263c" stroke-width="1.8"/></svg>Heating &amp; AC Repair</li>
  <li><svg class="check" width="16" height="16" viewBox="0 0 16 16"><rect x="1" y="2" width="12" height="12" fill="none" stroke="#d9263c" stroke-width="1.6"/><path d="M4 8l3 3 7-8" fill="none" stroke="#d9263c" stroke-width="1.8"/></svg>Hybrid Vehicle diagnostic &amp; repair</li>
</ul>
<ul class="abs service-list" style="left:767px;top:1799px">
  <li><svg class="check" width="16" height="16" viewBox="0 0 16 16"><rect x="1" y="2" width="12" height="12" fill="none" stroke="#d9263c" stroke-width="1.6"/><path d="M4 8l3 3 7-8" fill="none" stroke="#d9263c" stroke-width="1.8"/></svg>Insurance Claims</li>
  <li><svg class="check" width="16" height="16" viewBox="0 0 16 16"><rect x="1" y="2" width="12" height="12" fill="none" stroke="#d9263c" stroke-width="1.6"/><path d="M4 8l3 3 7-8" fill="none" stroke="#d9263c" stroke-width="1.8"/></svg>Leveling Kits &amp; Minor Lift Kit installation</li>
  <li><svg class="check" width="16" height="16" viewBox="0 0 16 16"><rect x="1" y="2" width="12" height="12" fill="none" stroke="#d9263c" stroke-width="1.6"/><path d="M4 8l3 3 7-8" fill="none" stroke="#d9263c" stroke-width="1.8"/></svg>Oil Changes</li>
  <li><svg class="check" width="16" height="16" viewBox="0 0 16 16"><rect x="1" y="2" width="12" height="12" fill="none" stroke="#d9263c" stroke-width="1.6"/><path d="M4 8l3 3 7-8" fill="none" stroke="#d9263c" stroke-width="1.8"/></svg>Pre Purchase Inspections</li>
  <li><svg class="check" width="16" height="16" viewBox="0 0 16 16"><rect x="1" y="2" width="12" height="12" fill="none" stroke="#d9263c" stroke-width="1.6"/><path d="M4 8l3 3 7-8" fill="none" stroke="#d9263c" stroke-width="1.8"/></svg>Radiators &amp; Fans Service &amp; Repair</li>
  <li><svg class="check" width="16" height="16" viewBox="0 0 16 16"><rect x="1" y="2" width="12" height="12" fill="none" stroke="#d9263c" stroke-width="1.6"/><path d="M4 8l3 3 7-8" fill="none" stroke="#d9263c" stroke-width="1.8"/></svg>State Inspection</li>
  <li><svg class="check" width="16" height="16" viewBox="0 0 16 16"><rect x="1" y="2" width="12" height="12" fill="none" stroke="#d9263c" stroke-width="1.6"/><path d="M4 8l3 3 7-8" fill="none" stroke="#d9263c" stroke-width="1.8"/></svg>Suspension Service &amp; Repair</li>
  <li><svg class="check" width="16" height="16" viewBox="0 0 16 16"><rect x="1" y="2" width="12" height="12" fill="none" stroke="#d9263c" stroke-width="1.6"/><path d="M4 8l3 3 7-8" fill="none" stroke="#d9263c" stroke-width="1.8"/></svg>Timing Belts &amp; Water Pumps</li>
  <li><svg class="check" width="16" height="16" viewBox="0 0 16 16"><rect x="1" y="2" width="12" height="12" fill="none" stroke="#d9263c" stroke-width="1.6"/><path d="M4 8l3 3 7-8" fill="none" stroke="#d9263c" stroke-width="1.8"/></svg>Tire Balance &amp; Rotations</li>
  <li><svg class="check" width="16" height="16" viewBox="0 0 16 16"><rect x="1" y="2" width="12" height="12" fill="none" stroke="#d9263c" stroke-width="1.6"/><path d="M4 8l3 3 7-8" fill="none" stroke="#d9263c" stroke-width="1.8"/></svg>Tires</li>
  <li><svg class="check" width="16" height="16" viewBox="0 0 16 16"><rect x="1" y="2" width="12" height="12" fill="none" stroke="#d9263c" stroke-width="1.6"/><path d="M4 8l3 3 7-8" fill="none" stroke="#d9263c" stroke-width="1.8"/></svg>Tune ups &amp; Factory Scheduled Maintenance</li>
  <li><svg class="check" width="16" height="16" viewBox="0 0 16 16"><rect x="1" y="2" width="12" height="12" fill="none" stroke="#d9263c" stroke-width="1.6"/><path d="M4 8l3 3 7-8" fill="none" stroke="#d9263c" stroke-width="1.8"/></svg>24-hr Night Drop</li>
</ul>
<p class="abs ask-band">Dont see a service you need? <a>Contact us</a></p>

<!-- CONTACT -->
<h2 class="abs contact-title">Contact us for a free estimate!</h2>
<p class="abs contact-copy">Please include year, model, and the service or repair you would like an estimate on.</p>
<p class="abs contact-alt">Want to make appointment instead?</p>
<a class="abs contact-click">Click Here</a>

<div class="abs field" style="left:606px;top:2405px;width:511px;height:43px">Name</div>
<div class="abs field" style="left:606px;top:2461px;width:249px;height:43px">Email Address</div>
<div class="abs field" style="left:869px;top:2461px;width:248px;height:43px">Phone</div>
<div class="abs field" style="left:606px;top:2517px;width:249px;height:43px">Model<svg width="10" height="6" viewBox="0 0 10 6"><path d="M1 1l4 4 4-4" fill="none" stroke="#444" stroke-width="1.3"/></svg></div>
<div class="abs field" style="left:869px;top:2517px;width:248px;height:43px">Year<svg width="10" height="6" viewBox="0 0 10 6"><path d="M1 1l4 4 4-4" fill="none" stroke="#444" stroke-width="1.3"/></svg></div>
<div class="abs field" style="left:606px;top:2573px;width:511px;height:43px">Services<svg width="10" height="6" viewBox="0 0 10 6"><path d="M1 1l4 4 4-4" fill="none" stroke="#444" stroke-width="1.3"/></svg></div>
<div class="abs field is-area" style="left:606px;top:2629px;width:511px;height:100px">Message</div>
<div class="abs submit">Submit</div>

<!-- GALLERY -->
<div class="abs tile" style="left:0;top:2867px;width:331px;height:222px" role="img" aria-label="White Mirabo SUV, front three-quarter view"></div>
<div class="abs gallery-card">
  <h2 class="abs gallery-title">Gallery</h2>
  <div class="abs gallery-btn">View More <svg width="14" height="12" viewBox="0 0 14 12"><path d="M1 6h11M7 1l5 5-5 5" fill="none" stroke="#fff" stroke-width="1.8"/></svg></div>
</div>
<div class="abs tile" style="left:690px;top:2867px;width:331px;height:222px" role="img" aria-label="White Mirabo pickup truck, front three-quarter view"></div>
<div class="abs tile" style="left:1035px;top:2867px;width:165px;height:222px" role="img" aria-label="White Mirabo SUV, partial view"></div>
<div class="abs tile is-engine" style="left:0;top:3102px;width:165px;height:220px" role="img" aria-label="Engine cover close-up"></div>
<div class="abs tile" style="left:179px;top:3102px;width:331px;height:220px" role="img" aria-label="White Mirabo pickup truck"></div>
<div class="abs tile is-engine" style="left:523px;top:3102px;width:332px;height:220px" role="img" aria-label="Engine cover close-up"></div>
<div class="abs tile" style="left:869px;top:3102px;width:331px;height:220px" role="img" aria-label="White Mirabo pickup truck"></div>

<!-- FOOTER -->
<footer class="abs footer" role="img" aria-label="Dark tyre tread texture background"></footer>
<div class="abs footer-brand"><span class="brand-dot"></span>VANTA</div>
<p class="abs copyright">© 2017 Vanta Automotive LLC</p>

<div class="abs info" style="top:3390px">
  <svg width="14" height="18" viewBox="0 0 14 18"><path d="M7 1a6 6 0 0 0-6 6c0 4.5 6 10 6 10s6-5.5 6-10a6 6 0 0 0-6-6z" fill="#fff"/><circle cx="7" cy="7" r="2.2" fill="#222226"/></svg>
  <span>418 Harbor Bend Loop #3 Ridgeford,<br>TX 75990</span>
</div>
<div class="abs info" style="top:3443px">
  <svg width="16" height="16" viewBox="0 0 16 16"><circle cx="8" cy="8" r="6.8" fill="none" stroke="#fff" stroke-width="1.6"/><path d="M8 4v4.5l3 1.8" fill="none" stroke="#fff" stroke-width="1.6"/></svg>
  <span>Monday - Friday,<br>8:30 am - 6:00 pm</span>
</div>
<div class="abs info" style="top:3496px">
  <svg width="16" height="16" viewBox="0 0 16 16"><path d="M3.5 1.5l2.5 3-1.5 2a9 9 0 0 0 5 5l2-1.5 3 2.5-1.5 2.5C7 15 1 9 1 3z" fill="#fff"/></svg>
  <span>Office: 555.301.2240<br>Cell: 555.301.7781</span>
</div>
<div class="abs info" style="top:3550px">
  <svg width="16" height="12" viewBox="0 0 16 12"><rect width="16" height="12" rx="1" fill="#fff"/><path d="M1 1l7 5 7-5" fill="none" stroke="#222226" stroke-width="1.4"/></svg>
  <span>hello@vantaautomotive.example</span>
</div>

<nav class="abs quick">
  <div class="quick-title">Quick Links</div>
  <div>Home</div>
  <div>Services</div>
  <div>Contact Us</div>
  <div>Gallery</div>
  <div>Schedule an Appointment</div>
</nav>

</body>
</html>
```